Menu Design Project for New Catering company

I would like to see my menus in a warm, inviting format. I prepare food for small intimate dinners, business lunches, picnics, parties, weddings and rehearsal dinners. I work with clients to help create their dream whether it includes items on my menu or to prepare very personal dishes that bring them warm memories of a special time or moment.

Target Market(s)

Organizations, wedding and or event planners

Industry/Entity Type

Catering

Requirements
Must have
• I would like to include the logo that is included in the attachment below. I also included a copy of the poster Lio Brenn created for me. I hope this helps. Please be creative. I am a very happy, cheerful person that enjoys cooking and having fun. I would like the design to represent my personality as well as my food. When I cater I treat my customers like an extension of my family and it comes across to them with everything I do for them. I hope this can somehow be reflected in your designs.
Should not have
• I'm open to all ideas and don't want to limit your creativity.

```html
<!DOCTYPE html>
<html lang="en">
<head>
<meta charset="utf-8">
<title>Buffet Menu Options</title>
<link href="https://fonts.googleapis.com/css2?family=Cabin+Sketch:wght@400;700&family=Roboto+Slab:wght@700&family=Open+Sans:ital,wght@0,400;0,700;1,400&family=Josefin+Sans:ital,wght@0,600;1,400&family=Lato:wght@400&display=swap" rel="stylesheet">
<style>
:root{
  --board:#2b2b2b;
  --board-dark:#1f1f1f;
  --chalk:#f2f2f2;
  --chalk-soft:#d8d8d8;
  --green:#3fae49;
  --green-deep:#2f8f3a;
  --tomato:#b3231f;
  --herb:#5c8c2e;
  --cinnamon:#8a4a22;
}
*{margin:0;padding:0;box-sizing:border-box}
html,body{width:1200px;height:777px;overflow:hidden;background:var(--board-dark)}
.menu{position:relative;width:1200px;height:777px;overflow:hidden;color:var(--chalk);
  background:
   linear-gradient(90deg,rgba(0,0,0,0) 590px,rgba(0,0,0,.35) 600px,rgba(0,0,0,0) 612px),
   radial-gradient(ellipse at 30% 40%,#353535 0%,#262626 75%),
   var(--board);}
.abs{position:absolute}
.chalk-title{font-family:'Cabin Sketch',cursive;color:var(--green);font-weight:400;letter-spacing:.5px}
.slab{font-family:'Roboto Slab',serif;font-weight:700}
.italic{font-family:'Open Sans',sans-serif;font-style:italic;font-weight:400}
.page-title{left:0;width:600px;top:16px;text-align:center;font-size:37px}
.page-title .flick{font-size:24px;color:var(--chalk-soft);vertical-align:middle}
.subtitle{left:0;width:600px;top:70px;text-align:center;font-size:15px}
.option-head{left:0;width:600px;text-align:center;font-family:'Open Sans',sans-serif;font-weight:700;font-size:12px;letter-spacing:.2px}
.option-head::before,.option-head::after{content:"";display:inline-block;width:22px;height:2px;background:var(--chalk);vertical-align:middle;margin:0 7px}
.option-text{left:16px;width:572px;font-size:11.2px;line-height:14px}
.banner{text-align:center}
.banner svg{position:absolute;left:0;top:0}
.banner span{position:relative;display:block;font-family:'Cabin Sketch',cursive;color:var(--green);font-size:30px;line-height:50px}
.price{left:0;width:600px;text-align:center;font-size:15px;line-height:19px}
.includes{left:10px;width:580px;text-align:center;font-size:10.8px;line-height:14.5px}
.dish-col{width:280px}
.dish{margin-bottom:9px}
.dish h3{font-family:'Roboto Slab',serif;font-size:13px;line-height:16px;margin-bottom:2px}
.dish p{font-family:'Open Sans',sans-serif;font-style:italic;font-size:11px;line-height:14px}
.col-rule{left:300px;top:503px;width:1px;height:250px;background:rgba(255,255,255,.35)}
.salad h3{font-family:'Roboto Slab',serif;font-size:13.5px;margin-bottom:2px}
.salad p{font-family:'Open Sans',sans-serif;font-style:italic;font-size:11px;line-height:14px}
.center-list{text-align:center}
.desserts{left:640px;width:226px;top:333px;font-family:'Josefin Sans',sans-serif;font-style:italic;font-size:15.5px;line-height:18px}
.apps-list{left:630px;width:246px;top:530px;font-family:'Josefin Sans',sans-serif;font-size:13.5px;line-height:16px}
.apps-list li{list-style:none;margin-bottom:7px}
.light{font-style:italic;font-weight:400}
.bold{font-weight:600;font-style:normal}
.sides{left:920px;width:246px;top:101px;font-family:'Josefin Sans',sans-serif;font-size:13.5px;line-height:16px}
.sides li{list-style:none;margin-bottom:7.6px}
.drinks{left:923px;width:218px;top:500px;font-family:'Roboto Slab',serif;font-size:12.5px;line-height:15.5px}
.drinks .row{display:flex;justify-content:space-between;margin-bottom:8px}
.tagline{left:620px;width:580px;top:702px;text-align:center;font-family:'Lato',sans-serif;color:var(--green);font-size:20px;line-height:23px}
.art{position:absolute}
</style>
</head>
<body>
<main class="menu">

  <div class="art" role="img" aria-label="Scattered red peppercorns" style="left:0;top:0;width:70px;height:72px;border-radius:0 0 60px 0;background:radial-gradient(circle at 30% 30%,#c83a2f,#7e1714 70%,transparent 72%)"></div>
  <div class="art" role="img" aria-label="Bundle of lemongrass stalks" style="left:530px;top:0;width:120px;height:70px;border-radius:40px;background:linear-gradient(160deg,#9fbf5a,#e6e2b8 70%,transparent);transform:rotate(-25deg);opacity:.85"></div>

  <h1 class="abs chalk-title page-title"><span class="flick">⁞</span> BUFFET MENU OPTIONS <span class="flick">⁞</span></h1>
  <h2 class="abs slab subtitle">CATERED SERVICE OPTIONS</h2>

  <h3 class="abs option-head" style="top:107px">OPTION 1 - INCLUDES BUFFET SUPPORT SERVICE</h3>
  <p class="abs italic option-text" style="top:125px">We want your event to be a huge success, so this may be exactly what you need. We will arrive to your event prior to meal, service, set-up and display your buffet including our buffet equipment, tablecloths for catered food tables. We will stay to maintain your buffet, keeping it clean and refreshed then depart immediately after meal service. Pricing also includes disposable dinnerware and cutlery. Additional charges for delivery and labor will be accessed and are based on the number of guests and number of support staff required. Quotes provided upon request.</p>

  <h3 class="abs option-head" style="top:218px">OPTION 2 - EXPRESS SERVICE</h3>
  <p class="abs italic option-text" style="top:236px">You may only require minimal support, in that case we can prepare and deliver your dinner in disposal equipment (pans, trays), disposable dinnerware and cutlery. We can provide disposable chafer equipment, and/or disposable tablecloths upon requests at costs. A delivery charge will be accessed to menu items listed below. Quotes available upon requests.</p>

  <div class="art" role="img" aria-label="Bowl of pulled pork salad with vegetables" style="left:-20px;top:300px;width:110px;height:130px;border-radius:50%;background:radial-gradient(circle,#b58a63 0%,#7a9a4a 45%,#e9e9e9 62%,#1a1a1a 70%)"></div>
  <div class="art" role="img" aria-label="Chalk sketch of garlic bulbs" style="left:492px;top:292px;width:52px;height:62px;border-radius:45% 45% 40% 40%;border:1.5px solid rgba(255,255,255,.55)"></div>
  <div class="art" role="img" aria-label="Sprig of fresh rosemary" style="left:460px;top:355px;width:112px;height:40px;border-radius:50%;background:linear-gradient(100deg,#3d6b24,#7ca84a);transform:rotate(28deg)"></div>

  <div class="abs banner" style="left:175px;top:308px;width:250px;height:50px">
    <svg width="250" height="50" viewBox="0 0 250 50" fill="none" stroke="#f2f2f2" stroke-width="1.5"><path d="M2 14h32v28H2l10-14z"/><path d="M248 14h-32v28h32l-10-14z"/><rect x="34" y="3" width="182" height="36" fill="#262626"/><rect x="38" y="7" width="174" height="28"/></svg>
    <span style="line-height:44px">BUFFET</span>
  </div>

  <p class="abs slab price" style="top:371px">$12.00 per person + tax<br>(see service options above)</p>

  <p class="abs slab includes" style="top:422px">Includes - 1 Entrée, 2 Sides, and a Dessert.<br>Quotes to add additional entrée(s) and/or sides are available upon request or if you don’t see exactly what you are looking for we will be happy to work with you to accommodate your requests.<br>Appetizers and drinks are priced separately below.</p>

  <section class="abs dish-col" style="left:14px;top:500px">
    <article class="dish"><h3>Lasagna Supreme Roll-up</h3><p>Lasagna noodles topped with ricotta, mozzarella and parmesan cheese, beef, sausage and pepperoni in a thick rich meat sauce</p></article>
    <article class="dish"><h3>Pork Tenderloin with Marsala<br>Mushroom Sauce</h3><p>Tender lightly breaded pork tenderloin medallions topped with delicious sautéed mushrooms all simmered in Marsala wine and heavy cream to develop a rich, decadent sauce</p></article>
    <article class="dish"><h3>Smothered Chicken</h3><p>Honey mustard grilled chicken breast topped with sautéed mushrooms, crispy bacon, Monterey and cheddar chicken served with a creamy honey mustard sauce</p></article>
  </section>
  <div class="abs col-rule"></div>
  <section class="abs dish-col" style="left:313px;top:500px">
    <article class="dish"><h3>Chicken Marsala</h3><p>A lightly breaded chicken breast topped with delicious sautéed mushrooms, simmered in Marsala wine and heavy cream for a delicious, memorable meal</p></article>
    <article class="dish"><h3>Grilled or Smoked Chicken Breasts</h3><p>Cooked as requested, plain or glazed with a nice, sweet southern BBQ sauce</p></article>
    <article class="dish"><h3>Pulled Pork BBQ</h3><p>Tender smoked shredded pork in a sweet, spicy BBQ sauce, buns (onions and dill pickles on the side)</p></article>
    <article class="dish"><h3>Taco Salad Bar</h3><p>Taco Seasoned Ground Beef, refried beans, lettuce, tomatoes, onions, jalapenos, cheese, sour cream, salsa, taco sauce, soft tacos and tortilla chips</p></article>
  </section>

  <!-- right page -->
  <div class="abs banner" style="left:642px;top:24px;width:250px;height:50px">
    <svg width="250" height="50" viewBox="0 0 250 50" fill="none" stroke="#f2f2f2" stroke-width="1.5"><path d="M2 14h32v28H2l10-14z"/><path d="M248 14h-32v28h32l-10-14z"/><rect x="34" y="3" width="182" height="36" fill="#262626"/><rect x="38" y="7" width="174" height="28"/></svg>
    <span style="line-height:44px">SALADS</span>
  </div>
  <div class="abs banner" style="left:920px;top:24px;width:250px;height:50px">
    <svg width="250" height="50" viewBox="0 0 250 50" fill="none" stroke="#f2f2f2" stroke-width="1.5"><path d="M2 14h32v28H2l10-14z"/><path d="M248 14h-32v28h32l-10-14z"/><rect x="34" y="3" width="182" height="36" fill="#262626"/><rect x="38" y="7" width="174" height="28"/></svg>
    <span style="line-height:44px">OTHER SIDES</span>
  </div>
  <div class="art" role="img" aria-label="Dried herbs" style="left:1160px;top:-10px;width:50px;height:50px;border-radius:50%;background:radial-gradient(circle,#7d9a3a,#4e6a22 70%,transparent 72%)"></div>

  <section class="abs salad" style="left:616px;top:103px;width:262px">
    <h3>Spinach Salad</h3>
    <p>Fresh Spinach, Red Onions, Candied Pecans and Strawberries (when strawberries are available and/or in season)</p>
    <h3 style="margin-top:9px">House Salad</h3>
    <p>Mixed Greens, Tomatoes, Carrots, Cucumbers, Croutons and Choice of two types of Dressing (Ranch, Honey Mustard, Italian, or Blue Cheese)</p>
  </section>
  <div class="art" role="img" aria-label="Bowl of fresh spinach leaves" style="left:868px;top:146px;width:70px;height:70px;border-radius:50%;background:radial-gradient(circle,#6fa33c,#3f7a22 60%,#e8e8e8 66%,#cfcfcf 72%)"></div>

  <ul class="abs center-list sides">
    <li class="light">Broccoli Casserole</li>
    <li class="bold">Honey Glazed Carrots</li>
    <li class="light">Old Fashioned Green Beans</li>
    <li class="bold">Potato Salad</li>
    <li class="light">Potatoes – Mashed, Baked or<br>Ranch Seasoned Roasted</li>
    <li class="bold">Roasted Mixed Vegetables</li>
    <li class="light">Southern Baked Beans</li>
    <li class="bold">Sweet Potato Casserole</li>
    <li class="light">Sweet Corn (Creamed, Skillet Fried<br>or Corn on the Cob)</li>
  </ul>
  <div class="art" role="img" aria-label="Steel kitchen whisk" style="left:1150px;top:195px;width:38px;height:115px;border-radius:50% 50% 10px 10px;background:linear-gradient(180deg,#d9d9d9,#777);opacity:.8;transform:rotate(-18deg)"></div>

  <div class="abs banner" style="left:628px;top:275px;width:250px;height:50px">
    <svg width="250" height="50" viewBox="0 0 250 50" fill="none" stroke="#f2f2f2" stroke-width="1.5"><path d="M2 14h32v28H2l10-14z"/><path d="M248 14h-32v28h32l-10-14z"/><rect x="34" y="3" width="182" height="36" fill="#262626"/><rect x="38" y="7" width="174" height="28"/></svg>
    <span style="line-height:44px">DESSERTS</span>
  </div>
  <p class="abs center-list desserts">Cheesecakes<br>Cream or Fruit Pies<br>Cupcakes</p>
  <div class="art" role="img" aria-label="Silver dinner fork" style="left:640px;top:340px;width:14px;height:78px;border-radius:6px;background:linear-gradient(90deg,#999,#eee,#888);transform:rotate(25deg)"></div>
  <div class="art" role="img" aria-label="Chalk sketch of bell peppers" style="left:928px;top:340px;width:56px;height:58px;border-radius:45%;border:1.5px solid rgba(255,255,255,.55)"></div>
  <div class="art" role="img" aria-label="Chalk sketch of garlic bulbs" style="left:1076px;top:342px;width:46px;height:46px;border-radius:45% 45% 40% 40%;border:1.5px solid rgba(255,255,255,.55)"></div>

  <div class="abs banner" style="left:628px;top:416px;width:250px;height:50px">
    <svg width="250" height="50" viewBox="0 0 250 50" fill="none" stroke="#f2f2f2" stroke-width="1.5"><path d="M2 14h32v28H2l10-14z"/><path d="M248 14h-32v28h32l-10-14z"/><rect x="34" y="3" width="182" height="36" fill="#262626"/><rect x="38" y="7" width="174" height="28"/></svg>
    <span style="line-height:44px">APPETIZERS</span>
  </div>
  <p class="abs slab center-list" style="left:620px;width:266px;top:472px;font-size:14px;line-height:24px">Priced per appetizer/per person<br>$4.00</p>
  <ul class="abs center-list apps-list">
    <li class="light">Sweet and Spicy Meatballs</li>
    <li class="bold">Pinwheels (various)<br>with salsas and/or dips</li>
    <li class="light">Stuffed Mushrooms</li>
    <li class="bold">Shrimp cocktails<br>with cocktail sauce</li>
  </ul>
  <div class="art" role="img" aria-label="Chalk sketch of a mushroom" style="left:640px;top:595px;width:36px;height:42px;border-radius:50% 50% 20% 20%;border:1.5px solid rgba(255,255,255,.55)"></div>
  <div class="art" role="img" aria-label="Chalk sketch of tomatoes" style="left:822px;top:630px;width:48px;height:55px;border-radius:50%;border:1.5px solid rgba(255,255,255,.55)"></div>

  <div class="abs banner" style="left:922px;top:416px;width:250px;height:50px">
    <svg width="250" height="50" viewBox="0 0 250 50" fill="none" stroke="#f2f2f2" stroke-width="1.5"><path d="M2 14h32v28H2l10-14z"/><path d="M248 14h-32v28h32l-10-14z"/><rect x="34" y="3" width="182" height="36" fill="#262626"/><rect x="38" y="7" width="174" height="28"/></svg>
    <span style="line-height:44px">DRINKS</span>
  </div>
  <p class="abs slab center-list" style="left:922px;width:250px;top:473px;font-size:13px">(Includes cups and ice)</p>
  <div class="abs drinks">
    <div class="row"><span>12 oz. canned Soft Drinks</span><span>$1.00 Ea</span></div>
    <div class="row"><span>16 oz. bottled water</span><span>$1.00 Ea</span></div>
    <div class="row"><span>Gallon Tea<br>(sweet or unsweetened)</span><span style="align-self:flex-end">$6.00 Ea</span></div>
  </div>
  <div class="art" role="img" aria-label="Cinnamon sticks with mint leaves" style="left:928px;top:618px;width:110px;height:44px;border-radius:14px;background:linear-gradient(90deg,var(--cinnamon),#b06a35 60%,#5f9a3a);transform:rotate(-14deg)"></div>
  <div class="art" role="img" aria-label="Cup of lemon tea with mint" style="left:1092px;top:594px;width:96px;height:96px;border-radius:50%;background:radial-gradient(circle,#b8661e 0%,#7a3a10 45%,#f4f4f4 52%,#d6d6d6 70%)"></div>

  <p class="abs tagline">Delicious Food, Excellent Service and Affordable Pricing<br>Catering parties, weddings, picnics, private dinners, lunches, etc</p>
</main>
</body>
</html>
```